Catering Menu Package

I currently have a complete menu package, which we have redesigned as far as content, now I need to it put together in a catalog type format. It is essentially 10-12 pages in length, and will be sent for print production. Upon receiving a final edit
Updates

I have added an example gif to the project.

I did this free hand this basically what I am looking for. please change text and type to whatever you think would look best. This is a total rough design so, feel free to change any and everything. The text for the page is on the word documents. If you need more images let me know I am in the process of getting as many images uploaded for your use.

Reason: I figured we got a late jump with questions, so i am extending a few days .

Target Market(s)

The target market is business who wish to have catered luncheons, breakfasts , meetings

Industry/Entity Type

Catering

Requirements
Must have
• I have attached a copy of the text that what we want in the package, our logo, and i have also attached a catering package of another company to give you an idea what the finished product will be
Should not have
• It should not look identical to the example catering packages, these are for some inspiration we want our own design with the same type of look and feel

```html
<!DOCTYPE html>
<html lang="en">
<head>
<meta charset="utf-8">
<title>Catering Menu – Light Breakfast &amp; Desserts</title>
<link rel="stylesheet" href="https://fonts.googleapis.com/css2?family=Cinzel:wght@500;700&family=PT+Sans:wght@700&family=Noto+Serif:ital@1&display=swap">
<style>
  :root{
    --backdrop:#ffffff;
    --page-top:#f9f0a8;
    --page-mid:#f7eeb0;
    --page-bottom:#ffffff;
    --title-orange:#e8641e;
    --rule-orange:#f07818;
    --heading-green:#b4c62a;
    --frame-green:#c8d266;
    --body-grey:#a59f92;
    --price-grey:#b3aca2;
    --brand-ink:#2b2b2b;
  }
  *{box-sizing:border-box;margin:0;padding:0}
  html,body{width:1200px;height:900px;overflow:hidden;background:var(--backdrop)}
  .spread{position:relative;width:1200px;height:900px}

  .page{position:absolute;overflow:hidden;
    background:linear-gradient(180deg,var(--page-top) 0%,var(--page-mid) 100%);
    box-shadow:0 2px 10px rgba(0,0,0,.18)}
  .page--breakfast{left:30px;top:22px;width:610px;height:820px}
  .page--desserts{left:462px;top:56px;width:650px;height:824px}

  .page-title{font-family:"Cinzel",serif;font-weight:700;color:var(--title-orange);
    font-size:24px;letter-spacing:2px;position:absolute}
  .menu-heading{font-family:"PT Sans",sans-serif;font-weight:700;color:var(--heading-green);
    font-size:16px;letter-spacing:.6px;line-height:20px;position:absolute}
  .menu-text{font-family:"Noto Serif",serif;font-style:italic;color:var(--body-grey);
    font-size:12.5px;line-height:17px;letter-spacing:1.1px;position:absolute}
  .price{font-family:"Noto Serif",serif;color:var(--price-grey);font-size:14px;
    letter-spacing:.5px;position:absolute;right:30px}

  .photo{position:absolute;z-index:2;border:6px solid var(--frame-green)}
  .side-foot{position:absolute;left:0;top:650px;width:174px;height:170px;background:var(--page-bottom)}
  .rule-v{position:absolute;z-index:1;left:172px;top:158px;width:4px;height:662px;background:var(--rule-orange)}
  .rule-h{position:absolute;z-index:1;left:0;top:606px;width:650px;height:4px;background:var(--rule-orange)}
  .white-foot{position:absolute;left:0;top:610px;width:650px;height:214px;background:var(--page-bottom)}

  .brand{position:absolute;z-index:2;display:flex;flex-direction:column;align-items:center;justify-content:center;gap:8px;background:#fff}
  .brand-mark{width:22px;height:22px;background:var(--title-orange)}
  .brand-name{font-family:"PT Sans",sans-serif;font-weight:700;color:var(--brand-ink);
    font-size:14px;line-height:16px;text-align:center;letter-spacing:.5px}
  .page--desserts .brand{left:0;top:608px;width:128px;height:184px;border:5px solid var(--frame-green)}
  .page--breakfast .brand{left:56px;top:650px;width:112px;height:160px}
</style>
</head>
<body>
<main class="spread">

  <section class="page page--breakfast">
    <div class="side-foot"></div>
    <div class="rule-v"></div>

    <h1 class="page-title" style="left:268px;top:42px">Light Breakfast</h1>

    <div class="photo" style="left:0;top:24px;width:180px;height:148px;background:linear-gradient(135deg,#8a7a5a,#c9a070,#6b7b50)" role="img" aria-label="Photo of a fresh fruit platter display"></div>
    <div class="photo" style="left:6px;top:182px;width:192px;height:136px;background:linear-gradient(160deg,#d8d8d8,#d79aa6,#c0708a)" role="img" aria-label="Photo of a pink dessert table setting"></div>
    <div class="photo" style="left:22px;top:346px;width:182px;height:140px;background:linear-gradient(150deg,#e6b7c4,#f5e8ec,#e5aabb)" role="img" aria-label="Photo of place cards with starfish"></div>
    <div class="photo" style="left:34px;top:498px;width:176px;height:130px;background:linear-gradient(140deg,#7a6a50,#b49a70,#6b7548)" role="img" aria-label="Photo of a buffet centerpiece arrangement"></div>

    <div class="brand">
      <span class="brand-mark"></span>
      <span class="brand-name">Meadowbrook<br>Table<br>Caterers</span>
    </div>

    <h2 class="menu-heading" style="left:300px;top:96px">Quick and Easy</h2>
    <p class="menu-text" style="left:206px;top:130px;width:400px">French Pastry, a Fresh Baked Gourmet Muffin and Whole Fresh Fruit (Featuring Local Apples and Peaches, California Oranges, or Bananas).</p>

    <h2 class="menu-heading" style="left:306px;top:188px">Fast Farmhouse</h2>
    <p class="menu-text" style="left:212px;top:222px;width:400px">Fresh baked Breakfast Bread and Muffins, Whipped Butter and House-made Strawberry Jam and Local Fruit Jellies, and Whole Fresh Fruit (Featuring Local Apples and Peaches, California Oranges, or Bananas).</p>

    <h2 class="menu-heading" style="left:316px;top:314px">Light and Lean</h2>
    <p class="menu-text" style="left:222px;top:352px;width:390px">Individual Yogurt, Fresh Fruit and House-made Granola.</p>

    <h2 class="menu-heading" style="left:320px;top:392px">New Yorker</h2>
    <p class="menu-text" style="left:228px;top:432px;width:390px">Brooklyn Bagel, Whipped Cream Cheese, House-made Strawberry Jam and Local Fruit Jellies, Whipped Butter, and Whole Fresh Fruit (Featuring Local Apples and Peaches, California Oranges, or Bananas). Add Smoked Salmon.</p>

    <h2 class="menu-heading" style="left:330px;top:526px">City Farmhouse</h2>
    <p class="menu-text" style="left:236px;top:566px;width:390px">Fresh Baked Buttery Biscuits, Muffins and Breakfast Breads, Brooklyn Bagels, Fresh Fruit (Featuring Local Apples, California Oranges, or Bananas), Butter and Cream Cheese, House-made Jam and Local Fruit Jellies.</p>

    <p class="menu-text" style="left:248px;top:722px;width:360px">All Prices are per Person, minimum order per item chosen.</p>
    <p class="menu-text" style="left:250px;top:768px;width:360px">Local Products used when available.</p>
  </section>

  <section class="page page--desserts">
    <h1 class="page-title" style="left:290px;top:60px">Desserts</h1>

    <h2 class="menu-heading" style="left:54px;top:104px">Homemade Cookies, Brownies &amp; Blondies</h2>
    <span class="price" style="top:120px">$X.XX per person</span>

    <h2 class="menu-heading" style="left:52px;top:126px">Dessert Miniatures</h2>
    <p class="menu-text" style="left:52px;top:150px;width:390px">Homemade Cookies, Brownies, Blondies, Petit Fours, Miniature Chocolate Mousse Cups &amp; Crème Puffs</p>
    <span class="price" style="top:184px">$X.XX per person</span>
    <p class="menu-text" style="left:50px;top:196px;width:390px">Strawberry Shortcake &amp; Chocolate Brownie Mousse Parfaits</p>
    <span class="price" style="top:210px">$X.XX per person</span>

    <h2 class="menu-heading" style="left:46px;top:242px">New York Style Cheesecake Bar</h2>
    <p class="menu-text" style="left:46px;top:264px;width:380px">With warm chocolate sauce, caramel, strawberries Cherries &amp; whipped topping</p>
    <span class="price" style="top:296px">$X.XX per person</span>

    <h2 class="menu-heading" style="left:42px;top:306px">Ice Cream Sundae Bar</h2>
    <p class="menu-text" style="left:42px;top:330px;width:390px">Hand Dipped Ice Cream Cups.Served With Toppings: Chopped Nuts, Chocolate Chips, Crushed Cocoa Crème Cookies,Rainbow Sprinkles, Cherries, Whipped Topping,Chocolate Syrup, Caramel, Pineapple, Strawberry</p>

    <h2 class="menu-heading" style="left:36px;top:430px">Chocolate Fountain</h2>
    <p class="menu-text" style="left:36px;top:456px;width:410px">Milk Chocolate, Dark Chocolate Or White Chocolate. Marshmallows, Fresh Strawberries, Bananas, Pineapple, Cookies, Crisped Rice Treats, Pretzels, Angle Cake, Pound Cake</p>

    <div class="white-foot"></div>
    <div class="rule-h"></div>

    <div class="brand">
      <span class="brand-mark"></span>
      <span class="brand-name">Meadowbrook<br>Table<br>Caterers</span>
    </div>

    <div class="photo" style="left:132px;top:528px;width:168px;height:202px;background:linear-gradient(160deg,#5a3020,#8a5230,#c9a048)" role="img" aria-label="Photo of a chocolate fountain with fruit"></div>
    <div class="photo" style="left:256px;top:630px;width:236px;height:172px;background:linear-gradient(150deg,#d890a8,#f0c8d4,#c86a8a)" role="img" aria-label="Photo of pink cake pops on a dessert table"></div>
    <div class="photo" style="left:478px;top:548px;width:142px;height:196px;background:linear-gradient(150deg,#d64a4a,#f4e8dc,#7a2a28)" role="img" aria-label="Photo of petit fours on a platter"></div>
  </section>

</main>
</body>
</html>
```